Business Card Design

BrightHarbor is a fund management company that takes just four market positions a year. each position is linked to a big geopolitical and economic event happening in the world. So for example we may be buying gold mining stocks-these are the companies who dig the gold out of the ground, as all the gold is currently being bought by Asia, or buying the japanese stock market as this is one of the big stories of today.

I am looking for a logo that represents 'BrightHarbor'-the Bright Harbor.

I would like it to be small and sit to the left of the name of the company on the left hand side(I think!)on the top line of the business card please.

Industry/Entity Type

Mining

Contact Information for Business Card

BrightHarbor Capital management Ltd
41 Pellam Street
London E9T 2QN

Martin J Colby

Mob: 0(44)7823946250
Off: 0(44) 207 xxxx
email: mc@brightharbor-cm.example

```html
<!DOCTYPE html>
<html lang="en">
<head>
<meta charset="utf-8">
<title>BrightHarbor Capital Management Ltd – Business Card</title>
<link rel="stylesheet" href="https://fonts.googleapis.com/css2?family=Tinos&display=swap">
<style>
  :root {
    --paper: #ffffff;
    --ink: #111111;
    --brand-navy: #0d0d6e;
    --brand-green: #2a9a3c;
  }
  * { margin: 0; padding: 0; box-sizing: border-box; }
  html, body {
    width: 1200px;
    height: 800px;
    overflow: hidden;
    background: var(--paper);
  }
  .business-card {
    position: relative;
    width: 1200px;
    height: 800px;
    background: var(--paper);
    color: var(--ink);
    font-family: "Tinos", "Times New Roman", serif;
  }
  .brand-mark {
    position: absolute;
    left: 152px;
    top: 150px;
    display: flex;
    align-items: center;
    gap: 18px;
  }
  .brand-mark__dot {
    width: 70px;
    height: 70px;
    border-radius: 50%;
    background: var(--brand-navy);
  }
  .brand-mark__name {
    font-size: 34px;
    color: var(--brand-navy);
    line-height: 1;
  }
  .company-name {
    position: absolute;
    left: 157px;
    top: 306px;
    font-size: 44px;
    font-weight: 400;
    line-height: 1.1;
    white-space: pre;
  }
  .contact-block {
    position: absolute;
    left: 155px;
    font-size: 28px;
    line-height: 36px;
    font-style: normal;
  }
  .contact-block--address { top: 442px; }
  .contact-block--person { top: 550px; }
  .contact-block .label {
    display: inline-block;
  }
  .contact-block .label--office { width: 61px; }
</style>
</head>
<body>
  <main class="business-card">
    <div class="brand-mark">
      <span class="brand-mark__dot" aria-hidden="true"></span>
      <span class="brand-mark__name">BrightHarbor</span>
    </div>

    <h1 class="company-name">BrightHarbor Capital  Management Ltd</h1>

    <address class="contact-block contact-block--address">
      41 Pellam Street<br>
      London E9T 2QN
    </address>

    <address class="contact-block contact-block--person">
      Martin J Colby<br>
      <span class="label">Mob:</span> 0(44) 7823946250<br>
      <span class="label label--office">Off:</span>0(44) 207 xxxxxx<br>
      <span class="label">Email:</span> mc@brightharbor-cm.example
    </address>
  </main>
</body>
</html>
```